Presentation Folder Design - (Pocket Folder)

We are an accounting firm for dentists. We need a folder designed for our marketing material. Attached is our logo.

Industry/Entity Type

Accounting

```html
<!DOCTYPE html>
<html lang="en">
<head>
<meta charset="utf-8">
<title>Pocket Folder – Inside Spread</title>
<link rel="stylesheet" href="https://fonts.googleapis.com/css2?family=Arimo:wght@400;700&display=swap">
<style>
  :root {
    --page-bg: #f1f1f1;
    --panel-light: #ffffff;
    --panel-shade: #e3e5e8;
    --fold-line: #9a9a9a;
    --sheet-white: #ffffff;
    --sheet-edge: #b5b5b5;
    --rule-line: #8f8f8f;
    --heading-grey: #c9c9c9;
    --brand-blue: #b9dcea;
    --pocket-pink: #f6cdc4;
    --photo-tone-top: #e6b5aa;
    --photo-tone-bottom: #d9998b;
  }
  * { box-sizing: border-box; margin: 0; padding: 0; }
  html, body {
    width: 1200px; height: 849px; overflow: hidden;
    background: var(--page-bg);
    font-family: "Arimo", Arial, sans-serif;
  }
  .folder-spread {
    position: absolute; left: 90px; top: 60px;
    width: 1020px; height: 730px;
    display: flex;
  }
  .inside-left {
    position: relative; width: 510px; height: 100%;
    background: linear-gradient(90deg, var(--panel-light) 0%, var(--panel-shade) 100%);
    border-right: 1px dashed var(--fold-line);
  }
  .brand-name {
    position: absolute; left: 150px; top: 325px; width: 240px;
    display: flex; align-items: center; gap: 10px;
    color: var(--brand-blue); font-weight: 700; font-size: 26px; line-height: 1.15;
  }
  .brand-dot {
    flex: none; width: 16px; height: 16px; border-radius: 50%;
    background: var(--brand-blue);
  }
  .brand-text { white-space: nowrap; }
  .inside-right {
    position: relative; width: 510px; height: 100%;
    background: linear-gradient(90deg, var(--panel-shade) 0%, var(--panel-light) 30%, var(--panel-light) 100%);
  }
  .sheet {
    position: absolute; background: var(--sheet-white);
    border: 1px solid var(--sheet-edge);
  }
  .sheet--back { left: 18px; top: 0; width: 460px; height: 460px; }
  .sheet--mid  { left: 14px; top: 8px; width: 466px; height: 460px; }
  .sheet--front { left: 10px; top: 18px; width: 470px; height: 460px; padding: 22px 22px 0 24px; }
  .sheet-title {
    color: var(--heading-grey); font-weight: 700; font-size: 44px; letter-spacing: 0.5px;
  }
  .sheet-lines { list-style: none; margin-top: 22px; }
  .sheet-lines li { height: 20px; border-bottom: 1px solid var(--rule-line); }
  .pocket {
    position: absolute; left: 0; bottom: 0; width: 510px; height: 280px;
  }
  .pocket svg { display: block; width: 100%; height: 100%; }
</style>
</head>
<body>
  <main class="folder-spread">
    <section class="inside-left">
      <div class="brand-name">
        <span class="brand-dot"></span>
        <span class="brand-text">BrightRoot<br>Dental Accountants</span>
      </div>
    </section>
    <section class="inside-right">
      <div class="sheet sheet--back"></div>
      <div class="sheet sheet--mid"></div>
      <article class="sheet sheet--front">
        <h2 class="sheet-title">DOCUMENTS</h2>
        <ul class="sheet-lines">
          <li></li><li></li><li></li><li></li><li></li><li></li>
          <li></li><li></li><li></li><li></li><li></li><li></li>
          <li></li><li></li>
        </ul>
      </article>
      <div class="pocket">
        <svg viewBox="0 0 510 280" preserveAspectRatio="none">
          <defs>
            <linearGradient id="photoTone" x1="0" y1="0" x2="0" y2="1">
              <stop offset="0" stop-color="var(--photo-tone-top)"/>
              <stop offset="1" stop-color="var(--photo-tone-bottom)"/>
            </linearGradient>
          </defs>
          <path d="M0 60 Q255 -10 510 20 L510 280 L0 280 Z" fill="var(--pocket-pink)"/>
          <path role="img" aria-label="Photo of a smiling mouth with bright white teeth"
                d="M8 60 Q255 -14 505 22 Q470 230 250 250 Q60 240 8 60 Z"
                fill="url(#photoTone)"/>
        </svg>
      </div>
    </section>
  </main>
</body>
</html>
```